依頼詳細
WEB販売で高濃度アルコールのウェットシートを販売したいと考えております。
一般のお客様がこのチラシを見て購買意欲が出るような内容をお願い致します。
記載項目
①画像
・表面の商品画像(添付あり)

②文字
・裏面の注意事項(添付あり)
・アルコール75%
・除菌99.9%
・厚手シート
・除菌性能試験取得済
・拭くだけ簡単除菌!気になる菌・汚れに

③イラスト
・女性がテーブルやドアノブなどを拭いているイラスト
サイズ
A5
ページ数
両面
希望イメージ
シンプル 複雑
単色 カラフル
暗い 明るい
日常 高級
遊び心 厳粛
未来的 伝統的
女性的 男性的
希望する色
黄・オレンジ系、緑系、水色系
納品ファイル
• 高解像度JPG (.jpg)
• イラストレーター形式 (.ai)
補足説明
WEBで売られているウェットシートの広告のようなイメージです。
向きは縦でお願い致します。
■ 選んだ理由

分かりやすいデザインと使い方のピクトグラムが良かったので今回選ばせていただきました。

■ 提案者全員のお礼・コメント

皆様今回は弊社のデザインコンペにご参加くださり誠にありがとうございます。
どのデザインも素晴らしかったので決定するのが非常に難しかったです。

今後も不定期で依頼させていただきますのでご都合が合うようであれば是非ご参加ください。
引き続き宜しくお願い致します。

```html
<!DOCTYPE html>
<html lang="ja">
<head>
<meta charset="UTF-8">
<title>拭くだけで簡単除菌!</title>
<link href="https://fonts.googleapis.com/css2?family=M+PLUS+Rounded+1c:wght@700;800;900&family=Noto+Sans+JP:wght@500;700&display=swap" rel="stylesheet">
<style>
  :root {
    --cream: #fffbea;
    --sun: #fde58a;
    --sun-soft: #fff2bd;
    --orange: #f07a1e;
    --blue: #1f86d6;
    --white: #ffffff;
    --pack-green: #2fae5c;
    --pack-light: #eaf6ee;
  }
  * { margin: 0; padding: 0; box-sizing: border-box; }
  html, body { width: 847px; height: 1200px; overflow: hidden; }
  body { background: var(--cream); font-family: "Noto Sans JP", sans-serif; }
  .flyer {
    position: relative;
    width: 847px;
    height: 1200px;
    overflow: hidden;
    background: var(--cream);
  }
  .sun-shape { position: absolute; border-radius: 50%; }
  .sun-left { width: 520px; height: 520px; left: -230px; top: -250px; background: var(--sun); }
  .sun-right { width: 600px; height: 600px; right: -280px; top: -300px; background: var(--sun-soft); }
  .sun-bottom { width: 900px; height: 420px; left: -30px; bottom: -260px; background: var(--sun-soft); }

  .headline {
    position: absolute;
    top: 88px;
    left: 0;
    width: 100%;
    text-align: center;
    font-family: "M PLUS Rounded 1c", sans-serif;
    font-weight: 900;
    color: var(--orange);
    line-height: 1.22;
  }
  .headline-lead { display: block; font-size: 74px; letter-spacing: 2px; }
  .headline-main { display: block; font-size: 100px; letter-spacing: 4px; }
  .headline-main .mark { display: inline-block; transform: skewX(-10deg); }

  .product-visual {
    position: absolute;
    left: 60px;
    top: 380px;
    width: 510px;
    height: 690px;
    border-radius: 40px;
    transform: rotate(-6deg);
    background: linear-gradient(160deg, var(--pack-light) 0%, var(--white) 45%, var(--pack-green) 100%);
    box-shadow: 0 10px 24px rgba(0,0,0,0.08);
  }

  .feature-list {
    position: absolute;
    right: 0;
    top: 436px;
    width: 322px;
    list-style: none;
  }
  .feature {
    background: var(--blue);
    color: var(--white);
    border-radius: 22px 0 0 22px;
    padding: 18px 20px 18px 30px;
    margin-bottom: 40px;
    font-weight: 700;
    font-size: 25px;
    line-height: 1.45;
    text-align: center;
  }
  .feature small { font-size: 21px; }
</style>
</head>
<body>
  <main class="flyer">
    <div class="sun-shape sun-left"></div>
    <div class="sun-shape sun-right"></div>
    <div class="sun-shape sun-bottom"></div>

    <h1 class="headline">
      <span class="headline-lead">拭くだけで</span>
      <span class="headline-main">簡単除菌<span class="mark">!</span></span>
    </h1>

    <div class="product-visual" role="img" aria-label="除菌ウェットシート商品パッケージ画像(アルコール75%・99.9%除菌・厚手シート10枚入)"></div>

    <ul class="feature-list">
      <li class="feature">アルコール75%<br>99.9%除菌</li>
      <li class="feature">厚手シート<small>で</small><br>使いやすい!</li>
      <li class="feature">除菌性能試験<br>取得済</li>
    </ul>
  </main>
</body>
</html>
```